Website Design for recruiting company

We need a homepage mockup for a recruiting company focused on the legal industry. Use your creative talent to come up with something visually appeal and professional for this web-site.

We'd really like to see the maze from the logo incorporated into the design somehow. Please use the website mockup provided as inspiration for this project. We really like the layout and photos!

Target Market(s)

lawyers

Industry/Entity Type

Legal

Number of Pages Required

1 page

Font styles to use
Sans Serif

```html
<!DOCTYPE html>
<html lang="en">
<head>
<meta charset="utf-8">
<title>Harbor Point Legal Search</title>
<link href="https://fonts.googleapis.com/css2?family=Mulish:wght@300;400;600;700;800&display=swap" rel="stylesheet">
<style>
:root{
  --plum:#5c4a5d;
  --plum-dark:#4a3a4b;
  --ink:#1f1f1f;
  --text:#555;
  --muted:#8a8a8a;
  --paper:#ffffff;
  --mist:#f3f3f3;
  --sage:#dfe3dc;
  --night:#111111;
  --line:#d6d6d6;
}
*{box-sizing:border-box;margin:0;padding:0}
html,body{width:1200px;height:3216px;overflow:hidden}
body{font-family:"Mulish",Arial,sans-serif;color:var(--ink);background:var(--paper)}
a{color:inherit;text-decoration:none}

/* header */
.site-header{height:68px;border-top:4px solid var(--plum);display:flex;align-items:center;justify-content:space-between;padding:0 100px 0 112px;background:var(--paper)}
.brand{display:flex;align-items:center;gap:14px;font-size:22px;font-weight:400;color:var(--plum);letter-spacing:.3px}
.brand-mark{width:52px;height:52px;border-radius:50%;background:var(--plum)}
.main-nav{display:flex;gap:46px;font-size:16px;color:#333}
.main-nav a.active{color:var(--plum);font-weight:700;border-bottom:2px solid var(--plum);padding-bottom:4px}

/* hero */
.hero{position:relative;height:732px;display:flex;flex-direction:column;align-items:center;justify-content:center;color:#fff;text-align:center}
.hero-photo{position:absolute;inset:0;background:radial-gradient(ellipse at 50% 55%,#7e9a4a 0%,#5b7a33 40%,#3c5a26 75%,#2f4a22 100%)}
.hero-copy{position:relative;margin-top:250px}
.hero h1{font-size:64px;font-weight:800;letter-spacing:.5px;text-shadow:0 2px 8px rgba(0,0,0,.35)}
.hero p{font-size:38px;font-weight:400;text-shadow:0 2px 8px rgba(0,0,0,.35);margin-top:2px}
.hero-arrow{position:absolute;top:430px}
.hero-arrow.prev{left:30px}
.hero-arrow.next{right:30px}

/* search */
.job-search{height:128px;background:var(--sage);display:flex;align-items:center;justify-content:center;gap:24px}
.job-search h2{font-size:30px;font-weight:700;color:#2d2d2d;margin-right:6px}
.field{height:44px;background:#fff;border:1px solid #cfd3cc;font-size:14px;color:#777;padding:0 14px;display:flex;align-items:center}
.field.keyword{width:260px}
.field.zip{width:260px}
.btn{display:inline-flex;align-items:center;justify-content:center;background:var(--plum);color:#fff;font-weight:600;font-size:16px}
.btn.search{width:148px;height:44px}

/* about */
.about{height:512px;display:flex}
.about-photo{width:620px;height:512px;background:linear-gradient(120deg,#e8e6e2 0%,#cfc7bd 45%,#8d7f73 70%,#3b3b40 100%)}
.about-body{flex:1;padding:96px 100px 0 0;margin-left:0;position:relative}
.about-body h2{font-size:46px;font-weight:800;letter-spacing:1px;padding-left:0;margin-left:0}
.about-inner{padding-left:0;margin-left:0}
.about-rule{width:100%;height:2px;background:var:--line;background:#bdbdbd;margin:10px 0 24px}
.about-text{padding-left:0;max-width:470px;font-size:15px;line-height:1.75;color:var(--text)}
.about-wrap{margin-left:-6px;padding-left:0}
.btn.read{width:174px;height:48px;margin-top:40px}

/* news */
.whats-new{height:1112px;background:var(--mist);padding-top:48px}
.section-title{text-align:center;font-size:46px;font-weight:800;letter-spacing:1px}
.section-rule{width:150px;height:2px;background:#bdbdbd;margin:12px auto 0}
.job-list{width:816px;margin:40px auto 0;display:flex;flex-direction:column;gap:20px}
.job-card{height:176px;background:#fff;display:flex;box-shadow:0 2px 6px rgba(0,0,0,.08)}
.job-photo{width:260px;flex:none}
.job-info{flex:1;padding:18px 26px 0 28px}
.job-head{display:flex;justify-content:space-between;align-items:baseline}
.job-title{font-size:17px;font-weight:800;text-transform:uppercase;letter-spacing:.3px}
.job-id{font-size:13px;color:#555}
.job-desc{font-size:13px;line-height:1.6;color:var(--muted);margin-top:16px;max-width:440px}
.btn.apply{width:112px;height:36px;font-size:13px;margin-top:18px}

/* employers */
.employers{height:228px;background:var(--plum);color:#fff;text-align:center;padding-top:34px}
.employers h2{font-size:40px;font-weight:700;letter-spacing:.5px}
.employers p{font-size:15px;line-height:1.6;width:640px;margin:16px auto 0;color:#e9e2e8}
.employer-actions{display:flex;justify-content:center;gap:30px;margin-top:20px}
.btn.outline{background:transparent;border:1.5px solid #fff;height:46px;font-size:14px;letter-spacing:.5px;padding:0 24px}

/* footer */
.site-footer{height:436px;background:var(--night);color:#fff;text-align:center;padding-top:96px}
.footer-mark{width:120px;height:120px;border-radius:50%;background:#d9d9d9;margin:0 auto}
.footer-name{font-size:28px;font-weight:400;margin-top:28px;letter-spacing:.5px}
.footer-nav{display:flex;justify-content:center;gap:58px;font-size:15px;margin-top:38px}
.copyright{font-size:14px;margin-top:36px;color:#ddd}
</style>
</head>
<body>

<header class="site-header">
  <div class="brand"><span class="brand-mark"></span>harbor point legal search</div>
  <nav class="main-nav">
    <a class="active" href="#">Home</a>
    <a href="#">About Us</a>
    <a href="#">What's New</a>
    <a href="#">For Employers</a>
  </nav>
</header>

<section class="hero">
  <div class="hero-photo" role="img" aria-label="Aerial view of a circular hedge labyrinth cut into a green lawn"></div>
  <svg class="hero-arrow prev" width="26" height="60" viewBox="0 0 26 60" aria-hidden="true"><polyline points="22,4 4,30 22,56" fill="none" stroke="#fff" stroke-width="2.5"/></svg>
  <svg class="hero-arrow next" width="26" height="60" viewBox="0 0 26 60" aria-hidden="true"><polyline points="4,4 22,30 4,56" fill="none" stroke="#fff" stroke-width="2.5"/></svg>
  <div class="hero-copy">
    <h1>Start Here,</h1>
    <p>Let Our Experience Guide You</p>
  </div>
</section>

<section class="job-search">
  <h2>Find your perfect job :</h2>
  <div class="field keyword">Job Title or Keywords</div>
  <div class="field zip">Zip Code</div>
  <a class="btn search" href="#">Search Job</a>
</section>

<section class="about">
  <div class="about-photo" role="img" aria-label="Two lawyers in suits talking across a small table in a bright office"></div>
  <div class="about-body" style="padding-left:0">
    <div style="margin-left:0;padding-left:0">
      <div style="margin-left:0">
        <div class="about-wrap" style="margin-left:-50px;background:transparent">
          <h2 style="margin-left:50px">ABOUT US</h2>
          <div class="about-rule" style="margin-left:0"></div>
          <p class="about-text" style="margin-left:50px">Harbor Point Legal Search focuses on the permanent placement of attorneys with law firms and corporations in the New England area. Founded in 1982, Harbor Point Legal Search is the oldest attorney search firm in New England, and is ranked the number one legal recruiter in New England in the most recent survey conducted by The Counsel Review.</p>
          <a class="btn read" href="#" style="margin-left:50px">Read More</a>
        </div>
      </div>
    </div>
  </div>
</section>

<section class="whats-new">
  <h2 class="section-title">WHAT'S NEW</h2>
  <div class="section-rule"></div>
  <div class="job-list">
    <article class="job-card">
      <div class="job-photo" role="img" aria-label="Colleagues reviewing documents at a desk" style="background:linear-gradient(135deg,#c9d3dc,#7f8d99)"></div>
      <div class="job-info">
        <div class="job-head"><h3 class="job-title">In-House/Corporate/M&amp;A</h3><span class="job-id">Job Id: 3771</span></div>
        <p class="job-desc">Global medical technology leader seeks 5+ year specialist with major law firm training for a lead role on all transactions and related diligence work.</p>
        <a class="btn apply" href="#">Apply Now!</a>
      </div>
    </article>
    <article class="job-card">
      <div class="job-photo" role="img" aria-label="Team meeting around a conference table" style="background:linear-gradient(135deg,#d8d2c8,#8a7c70)"></div>
      <div class="job-info">
        <div class="job-head"><h3 class="job-title">Associate/Litigation</h3><span class="job-id">Job Id: 3778</span></div>
        <p class="job-desc">Global medical technology leader seeks 5+ year specialist with major law firm training for a lead role on all transactions and related diligence work.</p>
        <a class="btn apply" href="#">Apply Now!</a>
      </div>
    </article>
    <article class="job-card">
      <div class="job-photo" role="img" aria-label="Professionals shaking hands in a brick-walled office" style="background:linear-gradient(135deg,#c98f73,#6e4a3c)"></div>
      <div class="job-info">
        <div class="job-head"><h3 class="job-title">In-House/Biotech/Contracts</h3><span class="job-id">Job Id: 3777</span></div>
        <p class="job-desc">Global medical technology leader seeks 5+ year specialist with major law firm training for a lead role on all transactions and related diligence work.</p>
        <a class="btn apply" href="#">Apply Now!</a>
      </div>
    </article>
    <article class="job-card">
      <div class="job-photo" role="img" aria-label="Hands working on a laptop beside paperwork" style="background:linear-gradient(135deg,#e0dcd6,#9a948c)"></div>
      <div class="job-info">
        <div class="job-head"><h3 class="job-title">In-House Life Sciences / Securities</h3><span class="job-id">Job Id: 3773</span></div>
        <p class="job-desc">Global medical technology leader seeks 5+ year specialist with major law firm training for a lead role on all transactions and related diligence work.</p>
        <a class="btn apply" href="#">Apply Now!</a>
      </div>
    </article>
    <article class="job-card">
      <div class="job-photo" role="img" aria-label="Client signing a contract across a desk" style="background:linear-gradient(135deg,#b79a82,#5a4336)"></div>
      <div class="job-info">
        <div class="job-head"><h3 class="job-title">In-House/Senior Counsel/SW Licensing</h3><span class="job-id">Job Id: 3769</span></div>
        <p class="job-desc">Global medical technology leader seeks 5+ year specialist with major law firm training for a lead role on all transactions and related diligence work.</p>
        <a class="btn apply" href="#">Apply Now!</a>
      </div>
    </article>
  </div>
</section>

<section class="employers">
  <h2>FOR EMPLOYERS</h2>
  <p>Our unparalleled recruiting industry and legal experience have generated an extensive network of contacts throughout the legal community.</p>
  <div class="employer-actions">
    <a class="btn outline" href="#">FIND THE RIGHT CANDIDATE</a>
    <a class="btn outline" href="#">START HERE</a>
  </div>
</section>

<footer class="site-footer">
  <div class="footer-mark"></div>
  <div class="footer-name">harbor point legal search</div>
  <nav class="footer-nav">
    <a href="#">Home</a>
    <a href="#">About Us</a>
    <a href="#">What's New</a>
    <a href="#">For Employers</a>
  </nav>
  <p class="copyright">© Copyrights 2020 - HARBOR POINT LEGAL SEARCH All Rights Reserved.</p>
</footer>

</body>
</html>
```